Doctors Office Web Design

Name of the business is Lian-Hua Qiu M.D.
We need a web design that is attractive for women that want to see Dr. Lian-Hua Qiu for Obstetrician Gynecology and Pregnancy care. Dr. Qiu earned her degree from Harbor Crest Medical College of obstetrician gynecology. We want to attract women of child bearing ages to come to our offices for health, education, and pregnancies.

Please visit http://www.drqiucare-example.com/ to help you get a feel for who we are. We will be adding some pictures and logo in the next few days.

We are looking for to have pages for and tabs including
About Us- History, Our Staff, Dr. Qiu
Patient Information- Appointments, E-Prescriptions, Payments Accepted, Insurance
Health- General, Sexual, Mental, Affiliates
Pregnancy- Minimally invasive surgery(our specialty), 4-D Ultra Sound, Hospital Affiliations
Media- News,Pictures, Videos
Locations- Palmvale Office, Marlow Office

The colors we would like to use are pastel colors, magenta, and plum

Target Market(s)

Women of all ages with an emphasis on 25-65 year olds

Industry/Entity Type

Business

Requirements
Must have
• Needs to include a location for a our videos and pictures that I will submit shortly. We also want a map to our location or atleast a place for one.
Nice to have
• A place for a google map of our office locations.

```html
<!DOCTYPE html>
<html lang="en">
<head>
<meta charset="utf-8">
<title>Lian-Hua Qiu M.D</title>
<link href="https://fonts.googleapis.com/css2?family=Arimo:ital,wght@0,400;0,700;1,400&display=swap" rel="stylesheet">
<style>
:root{
  --plum:#5a3784;
  --plum-deep:#3d2463;
  --magenta:#e6287a;
  --blush:#fbe1e8;
  --mist:#e4e3df;
  --ink:#1f1a22;
  --body:#2b2b2b;
  --tan:#c4b9a6;
  --white:#ffffff;
}
*{margin:0;padding:0;box-sizing:border-box}
html,body{width:1200px;height:900px;overflow:hidden}
body{font-family:"Arimo",Arial,sans-serif;background:var(--blush);position:relative;color:var(--body)}
.site-header{position:absolute;left:0;top:0;width:1200px;height:302px;background:linear-gradient(90deg,#e2e1dd 0%,#e4e3df 40%,#ecebe8 100%)}
.hero-photo{position:absolute;left:470px;top:0;width:730px;height:302px;
  background:
    radial-gradient(ellipse 150px 170px at 42% 48%,rgba(196,210,228,.75) 0%,rgba(214,222,234,.45) 55%,rgba(255,255,255,0) 100%),
    radial-gradient(ellipse at 45% 40%,#f6f5f3 0%,#eeece9 50%,#e3e1dd 100%);
  -webkit-mask-image:linear-gradient(90deg,transparent 0,#000 90px);
  mask-image:linear-gradient(90deg,transparent 0,#000 90px)}
.brand{position:absolute;left:65px;top:32px;width:194px;text-align:center}
.brand-mark{width:194px;height:194px;border-radius:50%;background:var(--plum)}
.brand-name{margin-top:20px;font-size:19px;color:var(--plum);white-space:nowrap}
.main-nav{position:absolute;left:0;top:305px;width:1200px;height:44px;background:linear-gradient(#ffffff,#efedea);border-top:2px solid #fff;box-shadow:0 1px 2px rgba(0,0,0,.08)}
.main-nav a{position:absolute;top:13px;transform:translateX(-50%);font-size:15.5px;color:var(--plum);text-decoration:none;white-space:nowrap}
.main-nav a.active{font-weight:700;color:var(--plum-deep)}
.dropdown{position:absolute;left:278px;top:349px;width:184px;height:163px;background:linear-gradient(#f6f4f1,#efedea);box-shadow:0 2px 5px rgba(0,0,0,.18);z-index:5}
.dropdown a{display:block;height:36px;line-height:36px;padding-left:33px;font-size:13px;color:var(--ink);text-decoration:none}
.dropdown a:first-child{margin-top:14px}
.dropdown a.current{color:var(--magenta);background:#e9e6e2}
.card{position:absolute;background:var(--white)}
.news-grid{left:12px;top:367px;width:860px;height:312px}
.guest-column{left:12px;top:689px;width:860px;height:211px}
.thumb{position:absolute;width:137px;height:127px;background:linear-gradient(160deg,#dfe6ee 0%,#c9c2b6 45%,#8e8a5e 100%)}
.teaser{position:absolute;width:240px}
.teaser h3,.guest-column h3{font-size:13.5px;font-weight:700;color:var(--ink);margin-bottom:9px;white-space:nowrap}
.teaser p{font-size:12.3px;line-height:17.3px;color:var(--body);white-space:nowrap}
.read-more{display:inline-block;margin-top:4px;font-size:13px;font-style:italic;color:var(--plum-deep);text-decoration:none}
.column-tag{position:absolute;left:583px;top:0;width:277px;height:28px;background:var(--tan);color:var(--white);font-size:12.5px;line-height:28px;padding-left:13px;letter-spacing:.2px}
.column-tag span{color:var(--plum)}
.column-body{position:absolute;left:167px;top:30px;width:670px}
.column-body p{font-size:12.3px;line-height:17.3px;color:var(--body);white-space:nowrap}
.doctor-photo{position:absolute;left:884px;top:367px;width:302px;height:310px;background:linear-gradient(180deg,#f1f0ef 0%,#e7e4e2 40%,#f3a14a 70%,#f0962f 100%)}
.quote{position:absolute;left:884px;top:677px;width:302px;height:127px;background:var(--plum);padding:22px 0 0 30px;color:var(--white)}
.quote blockquote{font-size:19px;font-style:italic;line-height:25px}
.quote cite{display:block;margin-top:10px;font-style:normal;font-size:17px}
.contact{position:absolute;left:884px;top:816px;width:302px;height:84px;background:var(--white);padding:23px 0 0 31px;font-size:15.5px;font-weight:700;color:var(--ink);line-height:20px}
</style>
</head>
<body>
<header class="site-header">
  <div class="hero-photo" role="img" aria-label="Photo of a smiling baby in a pale blue outfit lying on soft white bedding"></div>
  <div class="brand">
    <div class="brand-mark"></div>
    <div class="brand-name">Lian-Hua Qiu M.D</div>
  </div>
</header>

<nav class="main-nav">
  <a class="active" href="#" style="left:100px">Home</a>
  <a href="#" style="left:216px">About us</a>
  <a href="#" style="left:374px">Patient Information</a>
  <a href="#" style="left:519px">Health</a>
  <a href="#" style="left:634px">Pregnancy</a>
  <a href="#" style="left:762px">Affiliations</a>
  <a href="#" style="left:882px">Media</a>
  <a href="#" style="left:1008px">Locations</a>
</nav>

<section class="card news-grid">
  <div class="thumb" role="img" aria-label="Photo of a pregnant woman outdoors in a meadow" style="left:14px;top:17px"></div>
  <article class="teaser" style="left:166px;top:17px">
    <h3>Pregnancy</h3>
    <p>Lorem ipsum dolor sit amet, consect-<br>etur adipiscing elit. Curabitur eu est<br>nisi. Morbi et est nec risus adipiscing<br>scelerisque at ut velit.</p>
    <a class="read-more" href="#">Read more</a>
  </article>
  <div class="thumb" role="img" aria-label="Photo of a pregnant woman outdoors in a meadow" style="left:431px;top:17px"></div>
  <article class="teaser" style="left:583px;top:17px">
    <h3>New technology update</h3>
    <p>Lorem ipsum dolor sit amet, consect-<br>etur adipiscing elit. Curabitur eu est<br>nisi. Morbi et est nec risus adipiscing<br>scelerisque at ut velit.</p>
    <a class="read-more" href="#">Read more</a>
  </article>
  <div class="thumb" role="img" aria-label="Photo of a pregnant woman outdoors in a meadow" style="left:14px;top:172px"></div>
  <article class="teaser" style="left:166px;top:172px">
    <h3>Getting an ultrasound</h3>
    <p>Lorem ipsum dolor sit amet, consect-<br>etur adipiscing elit. Curabitur eu est<br>nisi. Morbi et est nec risus adipiscing<br>scelerisque at ut velit.</p>
    <a class="read-more" href="#">Read more</a>
  </article>
  <div class="thumb" role="img" aria-label="Photo of a pregnant woman outdoors in a meadow" style="left:431px;top:172px"></div>
  <article class="teaser" style="left:583px;top:172px">
    <h3>Opening of new location</h3>
    <p>Lorem ipsum dolor sit amet, consect-<br>etur adipiscing elit. Curabitur eu est<br>nisi. Morbi et est nec risus adipiscing<br>scelerisque at ut velit.</p>
    <a class="read-more" href="#">Read more</a>
  </article>
</section>

<div class="dropdown">
  <a href="#">Appointments</a>
  <a href="#">E-Prescriptions</a>
  <a href="#">Payments Accepted</a>
  <a class="current" href="#">Insurance</a>
</div>

<section class="card guest-column">
  <div class="column-tag">GUEST COLUMN BY <span>NORA ELLISON</span></div>
  <div class="thumb" role="img" aria-label="Photo of a pregnant woman outdoors in a meadow" style="left:14px;top:29px;height:161px"></div>
  <div class="column-body">
    <h3>The first weeks</h3>
    <p>Lorem ipsum dolor sit amet, consectetur adipiscing elit. Maecenas id sapien lacus, a volutpat justo. Etiam odio quam,<br>varius sed lobortis sed, commodo vel risus. In hac habitasse platea dictumst. Vestibulum in sapien a justo malesuada<br>posuere. Fusce et dolor sed lacus facilisis molestie. Aenean venenatis, orci porta consectetur mattis, libero risus sodales<br>magna, non gravida leo orci sit amet tellus. Integer luctus ante a nunc vulputate accumsan. Aenean metus massa, facilisis<br>quis commodo et, porta nec lectus. Cum sociis natoque penatibus et magnis dis parturient montes, nascetur ridiculus<br>mus. Suspendisse at turpis sed nibh suscipit eleifend. Sed elementum tristique mi, in vestibulum nunc sollicitudin vel. Ut<br>sollicitudin sodales magna, eu tempus eros vehicula quis. Duis et tempus turpis.</p>
    <a class="read-more" href="#">Read more</a>
  </div>
</section>

<div class="doctor-photo" role="img" aria-label="Photo of a smiling doctor in orange scrubs with a stethoscope"></div>
<aside class="quote">
  <blockquote>“Lorem ipsum dolor sit amet, consectetur adipiscing elit.“</blockquote>
  <cite>Lian-Hua Qiu M.D</cite>
</aside>
<aside class="contact">Do you wish to meet dr. Qiu?<br>Call (555) 214-0398</aside>
</body>
</html>
```